The Harborline LLC Asset Classes

I'm looking for for two designs here to go into powerpoint and potentially as a standalone PDF. My company does wealth management.
Graphic Image #1
I break down the investment world into 4 broad categories
-Preservation
-Capital Markets
-Real Estate
-Alternatives
In each broad category, there are subcategories:
Preservation: cash, checking/savings accounts, money market accounts, CD's, and fixed annuities.
Capital Markets: Publicly traded stocks and bonds
Real Estate: single-family residence, retail, industrial, multifamily, and office
Alternatives: private equity, private credit, cryptocurrency, asset-backed loans, tax liens, oil & gas, litigation finance, and royalties
Graphic 2: Please see the bottom f page 1 of the Tidewater Slides PDF.
Just like in graphic one, you have 4 categories of the Capital Markets and their respective subcategories
Category 1: Domestic Stocks: Subcategories are Large, mid, and small size companies
Category 2: International Stocks: Subcategories are Large, Mid/Small and by region - Developed and Emerging
Category 3: Fixed Income: You have subcategories like corporate, municipal, government, domestic, international
Category 4: Alternatives: The subcategories are metals and real estate
---------------------
I'm looking to create a graphic (either pie chart, or a circle broken into parts or some other clever way to illustrate this) to clearly illustrate both of these universes in a clean, professional, slick manner.
Target Market(s)
Investors
Colors
Designer to choose colors to be used in the design.
Requirements
Must have
- Clean
- professional
- Easy to read
- Creative
- Visually appealling
Nice to have
- I have attached my logo and some marketing materials so you can get a feel of what I am doing. Maybe you can clean this up too!

```html
<!DOCTYPE html>
<html lang="en">
<head>
<meta charset="utf-8">
<title>Capital Markets – The Harborline LLC</title>
<link href="https://fonts.googleapis.com/css2?family=Montserrat:wght@700;800&family=Source+Sans+3:wght@400;500;600&display=swap" rel="stylesheet">
<style>
  :root{
    --page:#d9dadc;
    --slide-top:#ffffff;
    --slide-bottom:#a7b8cc;
    --title:#f5914a;
    --brand:#1b5f86;
    --ink:#2b2b2b;
    --card-light:#ffffff;
    --card-dark:#dcdde0;
    --green:#46ae46; --green-ink:#177a1c;
    --blue:#0a6aae; --blue-ink:#0f2e5a;
    --orange:#fd9834; --orange-ink:#d56a12;
    --grey:#a4a4a4; --grey-ink:#555555;
  }
  *{box-sizing:border-box;margin:0;padding:0}
  html,body{width:1200px;height:1000px;overflow:hidden;background:var(--page)}
  body{font-family:"Source Sans 3",sans-serif;color:var(--ink)}

  .slide{
    position:absolute;left:0;top:50px;width:1200px;height:900px;overflow:hidden;
    background:linear-gradient(to bottom,var(--slide-top) 0%,var(--slide-top) 30%,var(--slide-bottom) 100%);
  }
  .slide-title{
    position:absolute;left:48px;top:50px;
    font-size:46px;font-weight:400;color:var(--title);letter-spacing:.5px;line-height:56px;
  }
  .brand{
    position:absolute;right:50px;top:56px;display:flex;align-items:center;gap:10px;
    font-weight:600;font-size:30px;line-height:36px;color:var(--brand);
  }
  .brand-dot{width:28px;height:28px;border-radius:50%;background:var(--brand)}

  .asset{
    position:absolute;top:262px;width:190px;height:425px;
    border-radius:30px;border-left:4px solid var(--main);
    background:linear-gradient(to bottom,var(--card-light) 0%,var(--card-light) 40%,var(--card-dark) 100%);
    box-shadow:0 10px 14px -10px rgba(40,40,50,.45);
  }
  .asset--domestic{left:92px;--main:var(--green);--head:var(--green-ink)}
  .asset--international{left:364px;--main:var(--blue);--head:var(--blue-ink)}
  .asset--fixed{left:638px;--main:var(--orange);--head:var(--orange-ink)}
  .asset--alternatives{left:910px;--main:var(--grey);--head:var(--grey-ink)}

  .asset-title{
    position:absolute;left:0;top:20px;width:100%;height:102px;
    display:flex;align-items:center;justify-content:center;text-align:center;
    font-family:"Montserrat",sans-serif;font-weight:800;font-size:18px;line-height:22px;
    letter-spacing:1px;color:var(--head);text-transform:uppercase;
  }
  .asset-band{
    position:absolute;left:-4px;right:0;top:125px;height:96px;background:var(--main);
  }
  .asset-detail{
    position:absolute;left:0;top:230px;width:100%;height:150px;
    display:flex;align-items:center;justify-content:center;
    font-size:20px;line-height:23px;font-weight:500;color:var(--ink);
  }
  .asset-detail ul{list-style:none}
  .asset-detail li{position:relative;padding-left:11px}
  .asset-detail li::before{content:"•";position:absolute;left:0;top:0;font-size:13px}
</style>
</head>
<body>
<main class="slide">
  <h1 class="slide-title">Capital Markets</h1>
  <div class="brand"><span class="brand-dot"></span><span class="brand-name">The Harborline LLC</span></div>

  <section class="asset asset--domestic">
    <h2 class="asset-title">Domestic<br>Stocks</h2>
    <div class="asset-band"></div>
    <div class="asset-detail"><p>Large, mid,<br>and small<br>companies</p></div>
  </section>

  <section class="asset asset--international">
    <h2 class="asset-title">International<br>Stocks</h2>
    <div class="asset-band"></div>
    <div class="asset-detail"><ul><li>Large, mid/small</li><li>Developed and<br>Emerging regions</li></ul></div>
  </section>

  <section class="asset asset--fixed">
    <h2 class="asset-title">Fixed<br>Income</h2>
    <div class="asset-band"></div>
    <div class="asset-detail"><ul><li>Corporate</li><li>Municipal</li><li>Government</li><li>Domestic</li><li>International</li></ul></div>
  </section>

  <section class="asset asset--alternatives">
    <h2 class="asset-title">Alternatives</h2>
    <div class="asset-band"></div>
    <div class="asset-detail"><ul><li>Metals</li><li>Real Estate</li></ul></div>
  </section>
</main>
</body>
</html>
```